Dietetic office: Bright Plate

I want to give my business card a modern and warm look (which attracts the eye and has a reassuring side), which links dietetics to a moment of well-being. The front and back sides must be used (not just to put the logo on the front side)

The map should be eye-catching and easy to read. I don't necessarily want to have a plain background, which I find visually weighs down the maps.
I really like the square format of a business card with rounded edges which is different from what we are used to finding (and why not take this square diagonally?), however I am not closed to another format as long as I like the style.

Who am I? Mireille, 32 years old, Dietician and passionate about food since always. I am specialized in slimming and an expert in micro nutrition, which means that I take into account not only the nutritional balance while maintaining pleasure (if foods are present in the business card, I do not want some cliché things where there would just be fruits and vegetables, but really something more global), but also the psycho-emotional dimension that I will treat with food supplements based on plants, fruits or vegetables.

-----------------------------------------------------------------------------------

 Mention to appear on the card IN FRENCH (please be careful in case of translation that the use of words is correct):

Mireille DORAN
Dietician Nutritionist
Expert in Slimming and Micro-Nutrition

Slogan: I help you lose weight sustainably with pleasure and by reconciling your events

Catchphrases: Want to lose weight? Do you like going out? Do you have a lot of events? And is pleasure on your plate important to you?

Make an appointment on Rendiplan or on 06 41 58 30 92
mireille.brightplate@exemplo-mail.fr
Address: Health Center, Rue des Glycines, 13590 Castelvent
www.brightplate-exemple.fr
Friendwall + Picturo Logo

- The company logo has been uploaded for your viewing. Other file formats can be made available if required.
- I would like a place for a photo of me to be possible.

Good morning,
I want to have a business card that is both lively and warm. Which will easily catch the eye while being easy to read and make people understand that I am in the field of well-being.
I like the square side in business cards (and why not use them diagonally?), or a more classic but original one.
Both the front and back sides must be used (I don't want to have the logo on just one side)
I don't want to have a plain background, but rather something more muted (I really like the suggestion from "Reed Cloud Graphic Designer" for this)
the use of logo for telephone, mail, address, rendiplan, friendwall, pictu etc is possible in order to facilitate reading

Please follow the various elements of the brief regarding the text and use the French text as it is.

I like business cards preferably square (with the possibility of using them diagonally).
The map should be eye-catching and easy to read.
It must bring pep while having softness which brings back to the well-being side
The card must be used on the front and back for the different elements (I do not want to have only the logo on the front side)
The text must correspond to the brief (be careful with the translation which can sometimes be bad)
I don't want to have a plain blue or orange background. I really like the idea of the background from "Reed Cloud Graphic Designer"

You can if you wish use symbols for contacts, telephone, rendiplan, address, fw, pictu....

Target Market(s)

mainly women between 25 and 65 years old + men around 40 years old

Contact Information for Business Card

Font styles to use
Sans Serif
Script

Colors
0054AA
0677BA
7BADD7
CADEEF
E8F1F8
0094D4
00A9DD
6FCCEA
C7EBF8
E9F6FB
00AB8E
00BBA5
67D7C9
C6EFE9
E9F9F6
FFC000
F8CF3A
FAE287
FDF2CF
FEFAEE
F0912C
F2A743
F7CA91
FBE8D2
FDF5EE

Requirements
Must have
• some pep! while being refined
Nice to have
• I really like the square format of a business card with rounded edges which is different from what we are used to finding, however I am not closed to another format as long as I like the style.
Should not have
• if foods are represented, only show fruits and vegetables (too cliché)

```html
<!DOCTYPE html>
<html lang="fr">
<head>
<meta charset="utf-8">
<title>Bright Plate – cartes de visite</title>
<link rel="stylesheet" href="https://fonts.googleapis.com/css2?family=Philosopher:wght@400;700&family=PT+Sans+Narrow&display=swap">
<style>
  :root {
    --blue-deep: #0054AA;
    --blue: #0677BA;
    --teal: #00AB8E;
    --pink: #E0399A;
    --ink: #111111;
    --backdrop: #e5e5e5;
    --card: #ffffff;
  }
  * { margin: 0; padding: 0; box-sizing: border-box; }
  html, body { width: 1200px; height: 724px; overflow: hidden; background: #fff; }
  .stage {
    position: absolute; left: 12px; top: 14px; width: 1175px; height: 710px;
    background: var(--backdrop);
  }
  .card {
    position: absolute; background: var(--card); border-radius: 52px;
    box-shadow: 0 8px 22px rgba(0,0,0,0.28);
    font-family: "Philosopher", sans-serif; text-align: center;
  }
  .card--front { left: 73px; top: 73px; width: 528px; height: 483px; }
  .card--back  { left: 627px; top: 83px; width: 508px; height: 483px; }
  .line { position: absolute; left: 0; right: 0; white-space: nowrap; }

  .brand { font-family: "Philosopher", sans-serif; font-weight: 700; color: var(--blue); }

  .front-brand { top: 52px; font-size: 44px; line-height: 52px; }
  .name { top: 152px; font-size: 31px; line-height: 36px; color: var(--blue); }
  .title { top: 186px; font-size: 24px; line-height: 30px; color: var(--teal); }
  .speciality { top: 220px; font-size: 24px; line-height: 30px; color: var(--pink); }
  .slogan { top: 257px; font-size: 17px; line-height: 21px; color: var(--ink); }

  .appointment-band {
    position: absolute; left: 0; top: 314px; width: 516px; height: 29px;
    background: var(--blue-deep); color: #fff;
    font-family: "PT Sans Narrow", sans-serif; font-size: 19px; line-height: 29px;
  }
  .contact { font-size: 15px; line-height: 20px; color: var(--ink); }
  .contact--email { top: 358px; }
  .contact--address { top: 381px; }
  .contact--web { top: 404px; }

  .social-row {
    position: absolute; left: 0; right: 0; top: 437px; height: 16px;
    display: flex; align-items: center; justify-content: center; gap: 10px;
  }
  .social-rule { width: 124px; height: 1px; background: var(--ink); }
  .social-name { font-size: 13px; color: var(--blue); }

  .back-brand { top: 214px; font-size: 68px; line-height: 76px; }
</style>
</head>
<body>
  <div class="stage">
    <section class="card card--front">
      <div class="line brand front-brand">Bright Plate</div>
      <div class="line name">Mireille DORAN</div>
      <div class="line title">Dietician Nutritionist</div>
      <div class="line speciality">Expert in Slimming and Micro-Nutrition</div>
      <div class="line slogan">I help you lose weight sustainably with<br>pleasure and by reconciling your events</div>
      <div class="appointment-band">Make an appointment on Rendiplan or on 06 41 58 30 92</div>
      <div class="line contact contact--email">mireille.brightplate@exemplo-mail.fr</div>
      <div class="line contact contact--address">Health Center, Rue des Glycines, 13590 Castelvent</div>
      <div class="line contact contact--web">www.brightplate-exemple.fr</div>
      <div class="social-row">
        <span class="social-rule"></span>
        <span class="social-name">Friendwall</span>
        <span class="social-name">Picturo</span>
        <span class="social-rule"></span>
      </div>
    </section>

    <section class="card card--back">
      <div class="line brand back-brand">Bright Plate</div>
    </section>
  </div>
</body>
</html>
```